High-End Medical Center Website Design Project

This design is part of a well thought-out project by an experienced project manager / developer. The approved wireframe is attached. Creative interpretations / suggestions based on the layout encouraged.

The design is for a new state-of-the-art medical center located in Dallas, Texas. The target audience would likely be individuals (approx. 60% female /40% male) who are the healthcare decision-makers for their families. They would likely have insurance and be inclined to seek out top-quality care.

Potential clients would choose this client over others in their industry because the medical center is physician owned, meaning it is patient-focused rather than profit-focused. The facility is brand new, featuring the latest technology. (This includes an amazing waiting room featuring WiFi and docking stations.) The physicians are hand-picked by referral only.

The look of the site should be extremely clean. We are going for a well-organized, professional look with a bit of a warm glow (interpret that however you like). Use crisp corners and the colors in the logo.

Think modern, clean with some great use of color / font.

We can get lovely photography of the medical center once construction is complete. Feel free to use an "example image" behind the Featured Area ("Physician Owned. Patient-Focused") if you like. We are open to ideas.

ONE CHANGE REQUESTED IN THE WIREFRAME:

Remove the "Connect" 1/4 page footer area and replace with a quick contact form. You may swap the "Locations" area with the form if desired. Put social media icons at the top left of the page in the top header area.

(Note: Please use social media icons that match the design rather than standard icons. We preferred not placing the icons at the top, but the client requested this. Let's not bring more attention to them than necessary.)
Updates

We're custom programming this site, so there's no need to base it on a template. Also, we would prefer not to use typical "seen everywhere" stock images.Thanks.

Industry/Entity Type

Construction

Requirements
Must have
• Follow the wireframe. This has been approved.
Nice to have
• Examples of what hover states, links or dropdowns might look like.

```html
<!DOCTYPE html>
<html lang="en">
<head>
<meta charset="utf-8">
<title>Nova Medical Center</title>
<link href="https://fonts.googleapis.com/css2?family=Montserrat:wght@400;600;700&family=Open+Sans:wght@400;600;700;800&display=swap" rel="stylesheet">
<style>
:root{
  --blue:#0a5cad;
  --blue-dark:#084f96;
  --teal:#3ba8b4;
  --orange:#ef5f2b;
  --ink:#1d1d1d;
  --text:#3a3a3a;
  --muted:#6d6d6d;
  --panel:#ececec;
  --white:#ffffff;
}
*{margin:0;padding:0;box-sizing:border-box}
html,body{width:782px;height:1200px;overflow:hidden}
body{position:relative;background:var(--white);font-family:Arial,"Open Sans",sans-serif;color:var(--ink)}
.abs{position:absolute}

/* header */
.topbar{left:0;top:0;width:782px;height:65px;background:var(--blue)}
.brand{left:113px;top:18px;display:flex;align-items:center;gap:8px;color:var(--white);font-family:"Montserrat",sans-serif;font-weight:700;font-size:22px;letter-spacing:1px}
.brand-mark{width:14px;height:14px;background:var(--teal)}
.call{left:528px;top:16px;display:flex;align-items:center;gap:8px;color:var(--white);font-family:"Open Sans",sans-serif;font-weight:700}
.call small{display:block;font-size:10px;line-height:12px}
.call strong{display:block;font-size:13px;line-height:15px}

.nav{left:0;top:65px;width:782px;height:31px;background:var(--white);border-bottom:1px solid #ddd}
.nav a{position:absolute;top:0;height:31px;line-height:31px;font-family:"Open Sans",sans-serif;font-weight:700;font-size:10.5px;color:#555;text-decoration:none;text-align:center}
.nav a.active{background:var(--teal);color:var(--white)}

/* hero */
.hero{left:0;top:96px;width:782px;height:320px;background:linear-gradient(180deg,#8fb4d2 0%,#b7c6d2 45%,#7a6a58 80%,#8c7f70 100%)}
.hero h1{left:0;top:20px;width:782px;text-align:center;font-family:"Open Sans",sans-serif;font-weight:800;font-size:28px;letter-spacing:-1px;color:var(--white);text-shadow:0 1px 3px rgba(0,0,0,.3)}
.hero p{left:0;top:54px;width:782px;text-align:center;font-size:13px;color:var(--white)}
.photo-circle{width:174px;height:174px;border-radius:50%;border:6px solid var(--white);box-shadow:0 2px 6px rgba(0,0,0,.3)}
.photo-circle.center{border-color:var(--teal)}
.btn-hero{top:291px;height:29px;line-height:29px;color:var(--white);font-family:"Montserrat",sans-serif;font-weight:600;font-size:14px;text-align:center;letter-spacing:.5px}
.btn-hero.blue{background:var(--blue)}
.btn-hero.orange{background:var(--orange)}

/* features */
.features{left:0;top:416px;width:782px;height:250px;background:var(--panel);border-bottom:1px solid #dcdcdc}
.intro{left:115px;top:54px;width:124px;font-size:13px;line-height:16.5px;color:var(--ink)}
.divider{left:260px;top:33px;width:1px;height:179px;background:#cfcfcf}
.feature{width:120px;text-align:center}
.feature .icon{width:78px;height:78px;margin:0 auto;display:block}
.feature h3{margin-top:10px;font-family:"Montserrat",sans-serif;font-weight:600;font-size:11px;color:var(--ink)}
.feature p{margin:8px auto 0;width:104px;font-size:7.6px;line-height:10.8px;color:var(--ink)}
.pill{display:inline-block;margin-top:7px;width:56px;height:10px;line-height:10px;border-radius:5px;background:#6a6a6a;color:var(--white);font-size:5.5px}

/* content */
.content{left:0;top:666px;width:782px;height:292px;background:var(--white)}
.team-photo{left:113px;top:62px;width:139px;height:151px;background:linear-gradient(180deg,#d8e3ec,#9fb7cb)}
.caption{left:113px;top:195px;width:139px;height:18px;line-height:18px;background:rgba(80,80,80,.85);color:var(--white);font-size:8px;padding-left:7px}
.section-title{font-family:"Open Sans",sans-serif;font-weight:400;font-size:16.5px;color:#2f8ee0;letter-spacing:-.5px}
.body-text{font-size:8.3px;line-height:10.8px;color:var(--ink)}
.btn-small{height:13px;line-height:13px;background:var(--orange);color:var(--white);font-size:6.5px;text-align:center}
.avatar{left:510px;top:173px;width:34px;height:34px;background:linear-gradient(180deg,#e7d3c0,#c7a58b)}
.avatar-name{left:552px;top:173px;font-size:7.5px;color:#bbb}

/* footer */
.footer{left:0;top:958px;width:782px;height:211px;background:var(--panel)}
.col-title{top:48px;font-family:"Open Sans",sans-serif;font-weight:400;font-size:11px;color:var(--blue);padding-bottom:4px;border-bottom:2px solid var(--blue)}
.news-item{width:115px}
.news-item h4{font-size:7.8px;color:var(--teal);font-weight:700}
.news-item p{font-size:7.8px;line-height:10px;color:var(--text);margin-top:1px}
.news-item .meta{font-size:6.8px;color:var(--orange);margin-top:4px}
.blog-list{left:253px;top:75px;width:88px;list-style:none}
.blog-list li{font-size:7.8px;color:var(--text);height:17.5px;line-height:14px;border-bottom:1px dotted #bdbdbd;padding-left:2px}
.blog-list li::before{content:"› ";color:#444}
.field{left:380px;width:122px;background:var(--white);border:1px solid #c8c8c8;font-size:7.5px;color:#999;padding:3px 6px;z-index:2}
.contact-photo{left:508px;top:70px;width:50px;height:141px;background:linear-gradient(180deg,rgba(214,214,214,0) 0%,#dcdcdc 40%,#e3d6ca 100%);z-index:1}
.wait-badge{left:562px;top:77px;width:34px;height:34px;border-radius:50%;background:var(--teal);color:var(--white);text-align:center;line-height:34px;font-size:12px;font-family:"Open Sans",sans-serif;z-index:2}
.wait-text{left:602px;top:78px;width:68px;font-size:7.8px;line-height:11px;color:var(--text)}

.bottombar{left:0;top:1169px;width:782px;height:31px;background:var(--blue)}
.legal{left:113px;top:11px;font-size:7.2px;color:var(--white)}
.social{top:8px;width:16px;height:16px;border:1px solid var(--white);border-radius:50%}
</style>
</head>
<body>

<header class="abs topbar">
  <div class="abs brand"><span>NOVA MEDICAL CENTER</span><span class="brand-mark"></span></div>
  <div class="abs call">
    <svg width="38" height="26" viewBox="0 0 38 26" aria-hidden="true">
      <path d="M2 9c0-5 34-5 34 0v4h-8V9H10v4H2z" fill="#fff"/>
      <path d="M11 12h16l4 13H7z" fill="#fff"/>
      <circle cx="19" cy="18" r="4" fill="#0a5cad"/>
    </svg>
    <div><small>CALL NOW</small><strong>(214) 555 - 0136</strong></div>
  </div>
</header>

<nav class="abs nav">
  <a style="left:126px;width:74px" href="#">WHY NOVA..</a>
  <a class="active" style="left:212px;width:84px" href="#">PHYCISIANS</a>
  <a style="left:308px;width:86px" href="#">SPECIALITIES</a>
  <a style="left:408px;width:86px" href="#">INFORMATION</a>
  <a style="left:502px;width:76px" href="#">LOCATIONS</a>
  <a style="left:590px;width:66px" href="#">CONTACT</a>
</nav>

<section class="abs hero" role="img" aria-label="Medical center building exterior">
  <h1 class="abs">PHYSICIAN OWNED, PATIENT FOCUSED</h1>
  <p class="abs">Lorem ipsum dolor sit amet, consectetur adipisicing elit, sed do eiusmod tempor</p>
  <div class="abs photo-circle" style="left:113px;top:91px;background:linear-gradient(160deg,#e9ecef,#b9c9a8)" role="img" aria-label="Doctor reviewing a chart with a senior patient"></div>
  <div class="abs photo-circle center" style="left:304px;top:91px;background:linear-gradient(160deg,#f2f4f6,#c9d4dc)" role="img" aria-label="Team of physicians in white coats"></div>
  <div class="abs photo-circle" style="left:495px;top:91px;background:linear-gradient(160deg,#eef1f3,#b7cdd0)" role="img" aria-label="Physician consulting a patient"></div>
  <div class="abs btn-hero blue" style="left:240px;width:153px">GET IN TOUCH ★</div>
  <div class="abs btn-hero orange" style="left:394px;width:148px">LEARN MORE ★</div>
</section>

<section class="abs features">
  <p class="abs intro">Lorem ipsum dolor sit amet, consectetur adipisicing elit, sed do eiusmod tempor incididunt</p>
  <div class="abs divider"></div>

  <div class="abs feature" style="left:284px;top:34px">
    <svg class="icon" viewBox="0 0 78 78" aria-hidden="true">
      <circle cx="39" cy="39" r="36" fill="#fff" stroke="#0a5cad" stroke-width="4"/>
      <path d="M30 20v14c0 8 14 8 14 0V20M37 42v10c0 7 12 7 12 0v-6" fill="none" stroke="#0a5cad" stroke-width="3"/>
      <circle cx="49" cy="43" r="4" fill="none" stroke="#0a5cad" stroke-width="3"/>
    </svg>
    <h3>Technology</h3>
    <p>Lorem ipsum dolor sit amet, consectetur adipisicing elit, sed do eiusmod tempor incididunt ut labore</p>
    <span class="pill">READ MORE</span>
  </div>

  <div class="abs feature" style="left:421px;top:34px">
    <svg class="icon" viewBox="0 0 78 78" aria-hidden="true">
      <circle cx="39" cy="39" r="36" fill="#fff" stroke="#0a5cad" stroke-width="4"/>
      <rect x="19" y="28" width="40" height="28" rx="3" fill="#0a5cad"/>
      <rect x="32" y="22" width="14" height="7" rx="2" fill="none" stroke="#0a5cad" stroke-width="3"/>
      <circle cx="39" cy="42" r="8" fill="#fff"/>
      <path d="M39 37v10M34 42h10" stroke="#0a5cad" stroke-width="3"/>
    </svg>
    <h3>Qualuity of Care</h3>
    <p>Lorem ipsum dolor sit amet, consectetur adipisicing elit, sed do eiusmod tempor incididunt ut labore</p>
    <span class="pill">READ MORE</span>
  </div>

  <div class="abs feature" style="left:558px;top:34px">
    <svg class="icon" viewBox="0 0 78 78" aria-hidden="true">
      <circle cx="39" cy="39" r="36" fill="#fff" stroke="#0a5cad" stroke-width="4"/>
      <path d="M20 30l6 16h32l4-8" fill="none" stroke="#0a5cad" stroke-width="4"/>
      <path d="M28 40l10-10 12 8" fill="none" stroke="#0a5cad" stroke-width="5"/>
      <circle cx="30" cy="54" r="4" fill="#0a5cad"/>
      <circle cx="54" cy="54" r="4" fill="#0a5cad"/>
    </svg>
    <h3>Patient Experience</h3>
    <p>Lorem ipsum dolor sit amet, consectetur adipisicing elit, sed do eiusmod tempor incididunt ut labore</p>
    <span class="pill">READ MORE</span>
  </div>
</section>

<section class="abs content">
  <div class="abs team-photo" role="img" aria-label="Group of smiling physicians and nurses"></div>
  <div class="abs caption">Consectetur adipisicing elit,</div>

  <h2 class="abs section-title" style="left:263px;top:57px">What we do ?</h2>
  <p class="abs body-text" style="left:263px;top:81px;width:212px">Lorem ipsum dolor sit amet, consectetur adipisicing elit, sed do eiusmod tempor incididunt ut labore et dolore magna aliqua. Ut enim ad minim veniam, quis nostrud exercitation ullamco laboris nisi ut aliquip ex ea commodo consequat. Duis aute irure dolor in reprehenderit in voluptate velit esse cillum dolore eu fugiat nulla pariatur. Excepteur sint occaecat cupidatat non proident, sunt in culpa qui officia deserunt mollit anim id est laborum. Duis aute irure dolor in reprehenderit in voluptate velit esse cillum dolore eu fugiat nulla pariatur. Excepteur sint occaecat cupidatat non proident, sunt in culpa qui officia deserunt mollit anim id est laborum.</p>
  <div class="abs btn-small" style="left:263px;top:224px;width:62px">LEARN MORE</div>

  <h2 class="abs section-title" style="left:510px;top:57px">Testimonials</h2>
  <p class="abs body-text" style="left:510px;top:81px;width:162px">Lorem ipsum dolor sit amet, consectetur adipisicing elit, sed do eiusmod tempor incididunt ut labore et dolore magna aliqua. Ut enim ad minim veniam, quis nostrud exercitation ullamco laboris nisi ut aliquip ex ea commodo consequat.  quis nostrud exercitation ullamco laboris nisi</p>
  <div class="abs avatar" role="img" aria-label="Portrait of a reviewing physician"></div>
  <div class="abs avatar-name">Dr. Avery</div>
  <div class="abs btn-small" style="left:510px;top:224px;width:62px">LEARN MORE</div>
</section>

<footer class="abs footer">
  <h3 class="abs col-title" style="left:113px;width:91px">News</h3>
  <div class="abs news-item" style="left:113px;top:71px">
    <h4>Consectetur adipisicing</h4>
    <p>Lorem ipsum dolor sit amet sed adipisicing elit, sed do</p>
    <div class="meta">22 July, 2013 &nbsp;| &nbsp;Read More</div>
  </div>
  <div class="abs news-item" style="left:113px;top:129px">
    <h4>Consectetur adipisicing</h4>
    <p>Lorem ipsum dolor sit amet sed adipisicing elit, sed do</p>
    <div class="meta">22 July, 2013 &nbsp;| &nbsp;Read More</div>
  </div>

  <h3 class="abs col-title" style="left:251px;width:91px">Blog</h3>
  <ul class="abs blog-list">
    <li>Could Services</li>
    <li>Custom Programming</li>
    <li>Universities</li>
    <li>Instant Support</li>
  </ul>

  <div class="abs contact-photo" role="img" aria-label="Hand holding a stethoscope"></div>

  <h3 class="abs col-title" style="left:379px;width:122px">Quick Contact</h3>
  <div class="abs field" style="top:74px;height:17px">Name</div>
  <div class="abs field" style="top:94px;height:17px">Email</div>
  <div class="abs field" style="top:115px;height:46px">Comment</div>
  <div class="abs btn-small" style="left:380px;top:167px;width:73px;height:16px;line-height:16px;font-size:7.5px">CONTACT US</div>

  <h3 class="abs col-title" style="left:560px;width:105px">Average Wait Time</h3>
  <div class="abs wait-badge">01</div>
  <p class="abs wait-text">Consectetur adipisicing Lorem ipsum dolor sit amet sed adipisicing elit, sed do</p>
</footer>

<div class="abs bottombar">
  <p class="abs legal">All Right Reserved © Copyright with www.novamc.com &nbsp;- &nbsp;2013 &nbsp;&nbsp; Terms &nbsp;. &nbsp;Privacy Policy</p>
  <span class="abs social" style="left:562px"></span>
  <span class="abs social" style="left:584px"></span>
  <span class="abs social" style="left:606px"></span>
  <span class="abs social" style="left:628px"></span>
  <span class="abs social" style="left:650px"></span>
</div>

</body>
</html>
```